Online-Marketing Material für Immobilienmakler
Zielgruppe
Ich bin Immobilienmakler und beschäftige mich mit der Vermietung / Verkauf von Immobilien. Zielgruppe sind Käufer / Verkäufer bzw. Vermieter und Mieter
Aufgabenstellung
Das Design soll sich am bestehenden CI orientieren, gleichzeitig modern gestaltet werden. Hierbei geht es mir um die Erstellung von Desginvorlagen für Post in Social-Media-Kanälen, welche ich je nach Inhalt entsprechend anpassen kann.
Inbesondere soll es eine Vorlage für die Vorstellung von neuen Objekten geben, welche immer wieder genutzt werden kann und daher die Inhalte in Canva anpassbar sind.

```html
<!DOCTYPE html>
<html lang="de">
<head>
<meta charset="utf-8">
<title>hausgrund – Social-Media-Vorlagen</title>
<link href="https://fonts.googleapis.com/css2?family=Tinos:wght@400;700&display=swap" rel="stylesheet">
<style>
  :root {
    --green: #84b930;
    --green-light: #bcdb8f;
    --green-pale: #e6f0d7;
    --blue: #1b7fba;
    --white: #ffffff;
    --ink: #3a3a3a;
    --sky-a: #6f97bd;
    --sky-b: #a9c1d7;
    --facade: #f3e4c8;
  }
  * { margin: 0; padding: 0; box-sizing: border-box; }
  html, body { width: 1027px; height: 1200px; overflow: hidden; background: var(--white); }
  body { font-family: "Tinos", "Times New Roman", serif; font-weight: 700; }
  .canvas { position: relative; width: 1027px; height: 1200px; overflow: hidden; }
  .layer { position: absolute; left: 0; top: 0; width: 1027px; height: 1200px; }
  .abs { position: absolute; }

  .brand { position: absolute; display: flex; align-items: center; gap: 7px; transform: translateX(-50%); }
  .brand-square { width: 18px; height: 18px; background: var(--blue); }
  .brand-name { color: var(--green); font-size: 24px; font-weight: 700; letter-spacing: 0.3px; line-height: 1; }

  .photo { position: absolute; background: linear-gradient(120deg, var(--sky-a) 0%, var(--sky-b) 55%, var(--facade) 56%, var(--facade) 100%); }
  .frame { position: absolute; background: var(--green-light); }
  .vline { position: absolute; width: 3px; background: var(--white); }
  .dot { position: absolute; width: 8px; height: 8px; border-radius: 50%; background: var(--white); }

  .headline { position: absolute; color: var(--white); text-align: center; line-height: 1; }
  .button { position: absolute; display: flex; align-items: center; justify-content: center; color: var(--ink); font-size: 17px; }

  .sold-disc { position: absolute; border-radius: 50%; }
  .sold-text { position: absolute; color: var(--green); font-size: 42px; transform: rotate(-15deg); letter-spacing: 1px; }

  .contact-line { position: absolute; width: 200px; text-align: center; color: var(--ink); font-size: 20px; line-height: 28px; }

  .checklist { position: absolute; left: 34px; top: 1042px; list-style: none; }
  .checklist li { display: flex; align-items: center; height: 46px; color: var(--white); font-size: 20px; }
  .checklist svg { width: 30px; height: 30px; margin-right: 14px; }
</style>
</head>
<body>
<div class="canvas">

  <!-- background shapes -->
  <svg class="layer" viewBox="0 0 1027 1200" aria-hidden="true">
    <polygon points="0,67 334,118 334,594 0,594" fill="var(--green)"/>
    <polygon points="346,61 681,112 681,509 346,459" fill="var(--green)"/>
    <polygon points="693,62 1027,113 1027,594 693,594" fill="var(--blue)"/>
    <rect x="228" y="708" width="15" height="200" fill="var(--green-light)"/>
    <rect x="0" y="890" width="85" height="13" fill="var(--green-light)"/>
    <polygon points="346,1060 681,1109 681,1200 346,1200" fill="var(--green-light)"/>
    <polygon points="346,667 681,717 681,1109 346,1060" fill="var(--green)"/>
  </svg>

  <!-- Panel: Sold -->
  <div class="brand" style="left:167px; top:37px;"><span class="brand-square"></span><span class="brand-name">hausgrund</span></div>
  <div class="frame" style="left:75px; top:184px; width:243px; height:190px;"></div>
  <div class="photo" role="img" aria-label="Foto: Giebel eines hellen Wohnhauses vor blauem Himmel" style="left:34px; top:125px; width:268px; height:233px;"></div>
  <div class="sold-disc" style="left:61px; top:135px; width:214px; height:214px; background:rgba(255,255,255,0.3);"></div>
  <div class="sold-disc" style="left:77px; top:151px; width:182px; height:182px; background:rgba(255,255,255,0.75);"></div>
  <div class="sold-text" style="left:94px; top:218px;">SOLD</div>
  <div class="headline" style="left:0; top:390px; width:334px; font-size:29px; line-height:29.5px;">Erfahren Sie mehr<br>zu unseren aktuellen<br>Angeboten unter:</div>
  <div class="button" style="left:53px; top:510px; width:228px; height:50px; background:var(--green-pale);">www.hausgrund-immo.de</div>

  <!-- Panel: Contact -->
  <div class="brand" style="left:510px; top:30px;"><span class="brand-square"></span><span class="brand-name">hausgrund</span></div>
  <div class="headline" style="left:380px; top:114px; text-align:left; font-size:49px; line-height:44px;">Kontaktieren<br>Sie uns</div>
  <div class="frame" style="left:411px; top:222px; width:171px; height:272px;"></div>
  <div class="photo" role="img" aria-label="Porträtfoto des Maklers im dunklen Sakko vor dunklem Hintergrund" style="left:380px; top:231px; width:191px; height:261px; background:linear-gradient(160deg,#4a4a4a,#1c1c1c 70%);"></div>
  <div class="vline" style="left:570px; top:229px; height:265px;"></div>
  <div class="dot" style="left:567px; top:225px;"></div>
  <div class="contact-line" style="left:427px; top:506px;">+49 7123 4560110<br>Mo-Fr 09:00-18:00</div>

  <!-- Panel: FAQ -->
  <div class="brand" style="left:857px; top:35px;"><span class="brand-square"></span><span class="brand-name">hausgrund</span></div>
  <div class="headline" style="left:798px; top:142px; text-align:left; font-size:47px;">FAQs</div>
  <div class="headline" style="left:798px; top:201px; text-align:left; font-size:17px;">Rund ums Haus</div>

  <!-- Panel: Features -->
  <div class="brand" style="left:162px; top:628px;"><span class="brand-square"></span><span class="brand-name">hausgrund</span></div>
  <div class="photo" role="img" aria-label="Foto: Hausgiebel mit Sprossenfenstern vor blauem Himmel" style="left:0; top:658px; width:228px; height:232px; clip-path:polygon(0 0,100% 15%,100% 100%,0 100%);"></div>
  <div class="photo" role="img" aria-label="Foto: Hausgiebel aus anderer Perspektive" style="left:86px; top:850px; width:248px; height:350px;"></div>
  <div class="vline" style="left:85px; top:852px; height:160px;"></div>
  <div class="dot" style="left:82px; top:848px;"></div>
  <svg class="layer" viewBox="0 0 1027 1200" aria-hidden="true">
    <polygon points="0,996 334,1043 334,1063 0,1011" fill="var(--green-light)" opacity="0.65"/>
    <polygon points="0,1011 334,1063 334,1200 0,1200" fill="var(--green)"/>
  </svg>
  <ul class="checklist">
    <li><svg viewBox="0 0 30 30"><circle cx="15" cy="15" r="13" fill="none" stroke="#fff" stroke-width="1.6"/><path d="M9 15.5l4 4 8-9" fill="none" stroke="#fff" stroke-width="1.6"/></svg>Erstbezug</li>
    <li><svg viewBox="0 0 30 30"><circle cx="15" cy="15" r="13" fill="none" stroke="#fff" stroke-width="1.6"/><path d="M9 15.5l4 4 8-9" fill="none" stroke="#fff" stroke-width="1.6"/></svg>Nähe zur Schule</li>
    <li><svg viewBox="0 0 30 30"><circle cx="15" cy="15" r="13" fill="none" stroke="#fff" stroke-width="1.6"/><path d="M9 15.5l4 4 8-9" fill="none" stroke="#fff" stroke-width="1.6"/></svg>Inklusive Parkfläche</li>
  </ul>

  <!-- Panel: New listing -->
  <div class="brand" style="left:510px; top:637px;"><span class="brand-square"></span><span class="brand-name">hausgrund</span></div>
  <div class="frame" style="left:368px; top:770px; width:185px; height:219px;"></div>
  <div class="photo" role="img" aria-label="Foto: neues Einfamilienhaus, Giebel vor blauem Himmel" style="left:380px; top:744px; width:267px; height:233px;"></div>
  <div class="vline" style="left:379px; top:747px; height:229px;"></div>
  <div class="dot" style="left:376px; top:743px;"></div>
  <div class="dot" style="left:376px; top:972px;"></div>
  <div class="headline" style="left:393px; top:758px; text-align:left; font-size:46px;">NEW</div>
  <div class="headline" style="left:346px; top:997px; width:335px; font-size:29px; line-height:29px;">Einfamilienhaus in<br>Bestlage</div>
  <div class="button" style="left:378px; top:1110px; width:228px; height:50px; background:#f1f7e8;">Einen Blick hinein werfen</div>

  <!-- arrows -->
  <svg class="layer" viewBox="0 0 1027 1200" aria-hidden="true">
    <path d="M418 438 C372 455 364 520 402 540" fill="none" stroke="var(--blue)" stroke-width="9" stroke-linecap="round"/>
    <polygon points="410,497 432,540 392,546" fill="var(--blue)"/>
    <path d="M774 187 C728 205 726 262 766 282" fill="none" stroke="var(--white)" stroke-width="9" stroke-linecap="round"/>
    <polygon points="768,245 790,282 752,292" fill="var(--white)"/>
    <path d="M252 868 C290 850 290 800 252 786" fill="none" stroke="var(--green)" stroke-width="9" stroke-linecap="round"/>
    <polygon points="234,786 262,778 248,808" fill="var(--green)"/>
    <path d="M628 1046 C582 1064 582 1122 626 1142" fill="none" stroke="var(--blue)" stroke-width="9" stroke-linecap="round"/>
    <polygon points="625,1102 645,1142 606,1150" fill="var(--blue)"/>
  </svg>

</div>
</body>
</html>
```